Innovative Health and Beauty business needs a clean Brand Image -

We need a logo designed and packaging for a new company. We are developing safe, easy to use, and reliable products to help people in health and beauty industry. We would like creative, clean, and elegant branding to elevate brand integrity and customer service focus.

```html
<!DOCTYPE html>
<html lang="en">
<head>
<meta charset="utf-8">
<title>Lumera – Inflatable Shampoo Bowl Carton Dieline</title>
<link rel="stylesheet" href="https://fonts.googleapis.com/css2?family=Roboto:wght@300;400&family=Source+Sans+3:wght@400&display=swap">
<style>
  :root {
    --cut-line: #4a4a4a;
    --flap-blue: #71c0df;
    --panel-blue: #6dbde0;
    --pale-blue: #d6edf6;
    --aqua: #8eeaf3;
    --pink: #fb7aa8;
    --blush: #fcdde8;
    --sky: #4a9ce8;
    --ink: #1a1a1a;
    --soft-ink: #333;
    --grey-ink: #5a5a5a;
    --paper: #ffffff;
    --mist: #f4f8fd;
  }
  * { box-sizing: border-box; margin: 0; padding: 0; }
  html, body { width: 1072px; height: 1200px; overflow: hidden; background: var(--paper); }
  .dieline { position: relative; width: 1072px; height: 1200px; }

  .cut { position: absolute; border: 1px solid var(--cut-line); background: var(--paper); }
  .dust-flap { overflow: hidden; }
  .dust-flap .fill { position: absolute; left: 0; right: 0; background: var(--flap-blue); }
  .tuck-side { border-radius: 0 0 42px 42px; }
  .tuck-bottom { border-radius: 0 0 56px 56px; }

  .print-panel { position: absolute; left: 327px; width: 408px; height: 170px; overflow: hidden; border: 1px solid var(--cut-line); }
  .print-panel.flipped { transform: rotate(180deg); }

  .tag-band { position: absolute; left: 0; top: 0; width: 129px; height: 55px;
    background: linear-gradient(90deg, var(--sky) 0%, #a58fd0 40%, var(--pink) 75%);
    display: flex; align-items: center; justify-content: center;
    font: 400 11px "Source Sans 3", sans-serif; color: var(--paper); letter-spacing: -0.2px; }
  .hero-band { position: absolute; left: 129px; top: 0; right: 0; height: 113px;
    background: linear-gradient(90deg, var(--pale-blue) 0%, #c4eff6 50%, var(--aqua) 100%); }
  .product-title { position: absolute; left: 129px; right: 0; top: 17px; text-align: center;
    font: 300 16px "Roboto", sans-serif; color: var(--soft-ink); padding-left: 20px; }
  .photo-block { position: absolute; left: 0; top: 55px; width: 129px; height: 115px; background: var(--panel-blue); }
  .photo { position: absolute; left: 18px; top: 16px; width: 96px; height: 84px;
    background: linear-gradient(160deg, #e8ecee 0%, #c9a08c 50%, #5a8fc0 100%); }
  .info-band { position: absolute; left: 129px; top: 113px; right: 0; height: 57px;
    background: linear-gradient(90deg, var(--pale-blue) 0%, var(--pale-blue) 25%, #cfe3f8 30%, #e9e0f0 65%, var(--blush) 100%); }
  .contact { position: absolute; left: 218px; top: 128px;
    font: 400 9.5px/12.5px "Source Sans 3", sans-serif; color: var(--grey-ink); }
  .name-box { position: absolute; left: 129px; top: 56px; width: 148px; height: 57px;
    background: var(--paper); border: 1px solid #2a3a8c;
    display: flex; align-items: center; justify-content: center;
    font: 400 33px "Source Sans 3", sans-serif; color: var(--ink); letter-spacing: 1px; }
  .glow { position: absolute; border-radius: 50%; background: rgba(255,255,255,0.25); }

  .plain-panel { position: absolute; left: 327px; width: 408px; height: 170px;
    border: 1px solid var(--cut-line);
    background: radial-gradient(circle at 50% 50%, var(--paper) 0%, var(--mist) 70%); }
  .back-copy { position: absolute; left: 42px; top: 27px; width: 200px;
    font: 400 9.5px/12.6px "Source Sans 3", sans-serif; color: var(--ink); }
  .back-copy p + p { margin-top: 12px; }
  .back-name { position: absolute; left: 291px; top: 117px; width: 88px; height: 34px;
    border: 1px solid var(--ink); background: var(--paper);
    display: flex; align-items: center; justify-content: center;
    font: 400 21px "Source Sans 3", sans-serif; color: var(--ink); }
</style>
</head>
<body>
<div class="dieline">

  <!-- top dust flaps -->
  <div class="cut dust-flap" style="left:198px;top:188px;width:128px;height:146px;"><div class="fill" style="top:41px;bottom:0;"></div></div>
  <div class="cut dust-flap" style="left:736px;top:188px;width:128px;height:146px;"><div class="fill" style="top:41px;bottom:0;"></div></div>

  <!-- top printed panel -->
  <section class="print-panel" style="top:174px;">
    <div class="hero-band"></div>
    <div class="info-band"></div>
    <div class="tag-band">INNOVATIVE</div>
    <div class="photo-block"><div class="photo" role="img" aria-label="Photo of a smiling woman having her hair washed in an inflatable shampoo bowl"></div></div>
    <div class="glow" style="left:102px;top:28px;width:40px;height:40px;"></div>
    <div class="glow" style="left:254px;top:96px;width:40px;height:40px;"></div>
    <h1 class="product-title">INFLATABLE SHAMPOO BOWL</h1>
    <div class="name-box">LUMERA</div>
    <p class="contact">Lorem ipsum dolor sit<br>Address 123 4567</p>
  </section>

  <!-- front plain panel -->
  <div class="plain-panel" style="top:344px;"></div>

  <!-- middle dust flaps -->
  <div class="cut dust-flap" style="left:198px;top:514px;width:128px;height:170px;"><div class="fill" style="top:1px;height:105px;"></div></div>
  <div class="cut dust-flap" style="left:735px;top:514px;width:128px;height:170px;"><div class="fill" style="top:1px;height:105px;"></div></div>

  <!-- second printed panel, inverted -->
  <section class="print-panel flipped" style="top:514px;">
    <div class="hero-band"></div>
    <div class="info-band"></div>
    <div class="tag-band">INNOVATIVE</div>
    <div class="photo-block"><div class="photo" role="img" aria-label="Photo of a smiling woman having her hair washed in an inflatable shampoo bowl"></div></div>
    <div class="glow" style="left:102px;top:28px;width:40px;height:40px;"></div>
    <div class="glow" style="left:254px;top:96px;width:40px;height:40px;"></div>
    <h2 class="product-title">INFLATABLE SHAMPOO BOWL</h2>
    <div class="name-box">LUMERA</div>
  </section>

  <!-- side tuck flaps -->
  <div class="cut tuck-side" style="left:198px;top:684px;width:120px;height:134px;"></div>
  <div class="cut tuck-side" style="left:745px;top:684px;width:119px;height:134px;"></div>

  <!-- back panel -->
  <section class="plain-panel" style="top:684px;">
    <div class="back-copy">
      <p>Lorem ipsum dolor sit amet, consectetuer adipiscing elit, sed diam nonummy nibh euismod tincidunt ut laoreet dolore magna</p>
      <p>aliquam erat volutpat. Ut wisi enim ad minim veniam, quis nostrud exerci tation ullamcorper suscipit lobortis nisl ut aliquip</p>
    </div>
    <div class="back-name">LUMERA</div>
  </section>

  <!-- bottom tuck -->
  <div class="cut tuck-bottom" style="left:327px;top:854px;width:408px;height:170px;border-top:none;"></div>

</div>
</body>
</html>
```